Brand new website for global research and investment startup

We need a simple website, maybe 3 pages: landing page with business description, investment philosophy, team and contact info.
We have a logo already that can be incorporated. Please use the logo only, not the text
We like the color green, something along the lines of #3D6C32 as the main color.
We'd like to design the website with geometric shapes in gradations of the base color. The shapes should suggest "work in progress", "built to last (a long time)", "solidity" and "indestructibility". One idea floating in my head sees smaller features with icosahedron and dodecahedron shapes, and maybe larger structures like crystal lattices; but please feel free to be creative and imagine your own.

```html
<!DOCTYPE html>
<html lang="en">
<head>
<meta charset="utf-8">
<title>Verdant – Our Team</title>
<link href="https://fonts.googleapis.com/css2?family=Inter:wght@400;500;600;700&display=swap" rel="stylesheet">
<style>
:root{
  --green:#3d6c32;
  --green-bright:#4f8a3c;
  --green-accent:#5fa046;
  --green-title:#6cb34f;
  --green-dark:#1f3a1a;
  --green-deep:#142a14;
  --ink:#1e1e1e;
  --line:#e3e6e1;
  --footer:#232323;
  --paper:#ffffff;
  --board:#f4f5f3;
}
*{box-sizing:border-box;margin:0;padding:0}
html,body{width:1200px;height:800px;overflow:hidden;background:var(--board);font-family:"Inter",Arial,sans-serif;color:var(--ink)}
.board-label{position:absolute;top:8px;font-size:11px;font-weight:500;color:#222;text-align:center}
.screen{position:absolute;top:27px;height:759px;background:var(--paper);border:1px solid #d6d8d4;border-radius:6px;overflow:hidden}
.abs{position:absolute}
.brand{position:absolute;font-weight:700;color:var(--ink);letter-spacing:.2px}
.brand.light{color:#fff}
.burger{position:absolute;width:14px;height:10px;border-top:1.5px solid #222;border-bottom:1.5px solid #222}
.burger::after{content:"";position:absolute;left:0;right:0;top:3px;border-top:1.5px solid #222}
.hero{position:absolute;left:0;right:0;overflow:hidden;
  background:
    radial-gradient(ellipse 55% 70% at 78% 30%,rgba(196,170,120,.55) 0%,rgba(120,130,90,.35) 45%,rgba(0,0,0,0) 75%),
    radial-gradient(ellipse 40% 60% at 95% 70%,rgba(150,165,140,.45) 0%,rgba(0,0,0,0) 70%),
    linear-gradient(100deg,var(--green-deep) 0%,#1b361a 40%,#35522e 65%,#5c6c48 85%,#7c8466 100%)}
.hero-title{position:absolute;font-weight:700;color:#fff;line-height:1}
.hero-title span{color:var(--green-accent)}
.hero-sub{position:absolute;color:#fff;font-weight:500}
.hero-text{position:absolute;color:#e6ece4;line-height:1.55}
.btn{position:absolute;background:var(--green);color:#fff;font-weight:600;border-radius:20px;text-align:center;white-space:nowrap}
.btn.outline{background:var(--green-bright);border:1.5px solid #fff}
.eyebrow{position:absolute;left:0;right:0;text-align:center;color:var(--green);font-weight:700;letter-spacing:.3px}
.heading{position:absolute;left:0;right:0;text-align:center;font-weight:700;color:var(--green-dark);line-height:1.15}
.lead{position:absolute;text-align:center;color:#333;line-height:1.5}
.ornament{position:absolute;border-radius:50%;
  background:radial-gradient(circle at 45% 40%,rgba(190,205,170,.55) 0%,rgba(200,212,185,.3) 45%,rgba(255,255,255,0) 72%)}
.card{position:absolute;background:#fff;border:1px solid var(--line);border-radius:5px;box-shadow:0 2px 6px rgba(0,0,0,.07);text-align:center}
.portrait{position:absolute;border-radius:3px;background:linear-gradient(180deg,#eef0ec 0%,#e2e5df 55%,#4a5060 85%,#2a3240 100%)}
.card .name{position:absolute;left:0;right:0;font-weight:700;color:var(--green)}
.card .role{position:absolute;left:0;right:0;color:#444}
.card .bio{position:absolute;left:6px;right:6px;color:#333;line-height:1.45}
.dot{position:absolute;border-radius:50%;background:var(--green)}
.contact-band{position:absolute;left:0;right:0;overflow:hidden;
  background:
    radial-gradient(ellipse 30% 55% at 40% 35%,rgba(90,150,60,.75) 0%,rgba(60,110,45,.4) 50%,rgba(0,0,0,0) 80%),
    radial-gradient(ellipse 35% 40% at 92% 25%,rgba(150,175,195,.9) 0%,rgba(120,150,170,.5) 50%,rgba(0,0,0,0) 85%),
    radial-gradient(ellipse 45% 35% at 85% 100%,rgba(70,120,40,.95) 0%,rgba(50,95,35,.5) 55%,rgba(0,0,0,0) 90%),
    linear-gradient(110deg,var(--green-deep) 0%,var(--green-dark) 35%,#2c5226 55%,#4f6f5e 78%,#7d96a6 100%)}
.contact-title{position:absolute;font-weight:700;color:var(--green-title);line-height:1.2}
.contact-text{position:absolute;color:#e7ece5;line-height:1.5}
.contact-line{position:absolute;color:#fff;display:flex;align-items:center;white-space:nowrap}
.contact-line i{display:inline-block;border-radius:50%;background:var(--green-bright);margin-right:6px;flex:none}
.form-title{position:absolute;font-weight:700;color:var(--green-dark);display:flex;align-items:center;white-space:nowrap}
.form-title svg{margin-right:5px}
.field{position:absolute;border:1px solid #dfe2dc;border-radius:2px;background:#fff;color:#444;padding:3px 5px}
.footer{position:absolute;left:0;right:0;bottom:0;background:var(--footer);color:#ddd}
.footer h4{position:absolute;color:#fff;font-weight:600;white-space:nowrap}
.footer .links{position:absolute;line-height:1.75;color:#ccc;white-space:nowrap}
.footer .tag{position:absolute;line-height:1.5;color:#ddd}
.footer .copy{position:absolute;left:0;right:0;text-align:center;color:#ccc}
.social{position:absolute;display:flex}
.social span{border:1px solid #ddd;border-radius:50%;display:block}
.row{position:absolute;left:12px;right:12px;height:30px;background:#fff;border:1px solid var(--line);border-radius:4px;box-shadow:0 1px 4px rgba(0,0,0,.06)}
.row .portrait{left:5px;top:3px;width:22px;height:22px}
.row .name{position:absolute;left:33px;top:7px;font-size:6px;font-weight:700;color:var(--green)}
.row .role{position:absolute;left:33px;top:16px;font-size:5px;color:#444}
.row .dot{right:6px;top:10px;width:9px;height:9px}
</style>
</head>
<body>

<div class="board-label" style="left:12px;width:624px">Desktop (1920px)</div>
<div class="board-label" style="left:655px;width:334px">Tablet (834px)</div>
<div class="board-label" style="left:1011px;width:176px">Mobile (390px)</div>

<!-- DESKTOP -->
<section class="screen desktop" style="left:12px;width:624px">
  <div class="brand" style="left:20px;top:11px;font-size:13px">Verdant</div>
  <nav style="position:absolute;top:14px;left:275px;font-size:6px;color:#222">
    <span class="abs" style="left:0;white-space:nowrap">Business Description</span>
    <span class="abs" style="left:110px;white-space:nowrap">Investment Philosophy</span>
    <span class="abs" style="left:222px;border-bottom:1px solid #222;padding-bottom:2px">Team</span>
  </nav>
  <div class="btn" style="left:543px;top:9px;width:63px;height:18px;line-height:18px;font-size:6px">Contact Info</div>

  <div class="hero" style="top:35px;height:212px" role="img" aria-label="Hero photograph of a green glass lattice roof structure">
    <svg class="abs" style="left:0;bottom:0" width="624" height="70" viewBox="0 0 624 70" preserveAspectRatio="none"><path d="M0 70 L0 50 C150 48 400 35 624 4 L624 70 Z" fill="#fff"/><path d="M320 46 C440 36 545 22 624 6" stroke="#5fa046" stroke-width="3" fill="none"/></svg>
  </div>
  <div class="hero-title" style="left:63px;top:71px;font-size:31px">Our <span>Team</span></div>
  <div class="hero-sub" style="left:63px;top:104px;font-size:9.6px">Built on experience. Focused on outcomes.</div>
  <div class="hero-text" style="left:63px;top:122px;width:190px;font-size:7.6px">A multidisciplinary team with deep expertise in investments, operations, and value creation. Together, we build enduring value.</div>
  <div class="btn" style="left:63px;top:174px;width:81px;height:20px;line-height:20px;font-size:7px">Contact Now</div>

  <div class="ornament" style="left:70px;top:225px;width:62px;height:62px" role="img" aria-label="Faint wireframe icosahedron ornament"></div>
  <div class="ornament" style="left:490px;top:222px;width:64px;height:64px" role="img" aria-label="Faint wireframe icosahedron ornament"></div>
  <div class="eyebrow" style="top:233px;font-size:6px">OUR STRENGTH</div>
  <div class="heading" style="top:244px;font-size:16px">The People Behind Our Purpose</div>
  <div class="lead" style="left:180px;width:264px;top:266px;font-size:7.4px">We combine decades of experience across investments, strategy, operations and finance to deliver consistent, long-term value.</div>

  <div class="card" style="left:26px;top:300px;width:111px;height:158px">
    <div class="portrait" style="left:6px;top:5px;width:99px;height:68px" role="img" aria-label="Portrait of Elliot Marsh"></div>
    <div class="name" style="top:78px;font-size:8px">Elliot Marsh</div>
    <div class="role" style="top:91px;font-size:6px">Chief Executive Officer</div>
    <div class="bio" style="top:103px;font-size:6px">20+ years in investment leadership and value creation.</div>
    <div class="dot" style="left:50px;top:138px;width:11px;height:11px"></div>
  </div>
  <div class="card" style="left:142px;top:300px;width:105px;height:158px">
    <div class="portrait" style="left:5px;top:5px;width:95px;height:68px" role="img" aria-label="Portrait of Nora Whitfield"></div>
    <div class="name" style="top:78px;font-size:8px">Nora Whitfield</div>
    <div class="role" style="top:91px;font-size:6px">Chief Investment Officer</div>
    <div class="bio" style="top:103px;font-size:6px">Expert in private markets and portfolio management.</div>
    <div class="dot" style="left:47px;top:138px;width:11px;height:11px"></div>
  </div>
  <div class="card" style="left:253px;top:300px;width:108px;height:158px">
    <div class="portrait" style="left:5px;top:5px;width:98px;height:68px" role="img" aria-label="Portrait of Owen Sinclair"></div>
    <div class="name" style="top:78px;font-size:8px">Owen Sinclair</div>
    <div class="role" style="top:91px;font-size:6px">Head of Operations</div>
    <div class="bio" style="top:103px;font-size:6px">Operational excellence and driving scalable performance.</div>
    <div class="dot" style="left:48px;top:138px;width:11px;height:11px"></div>
  </div>
  <div class="card" style="left:367px;top:300px;width:111px;height:158px">
    <div class="portrait" style="left:5px;top:5px;width:101px;height:68px" role="img" aria-label="Portrait of Claire Holden"></div>
    <div class="name" style="top:78px;font-size:8px">Claire Holden</div>
    <div class="role" style="top:91px;font-size:6px">Chief Financial Officer</div>
    <div class="bio" style="top:103px;font-size:6px">Financial strategy, risk management and governance.</div>
    <div class="dot" style="left:50px;top:138px;width:11px;height:11px"></div>
  </div>
  <div class="card" style="left:485px;top:300px;width:113px;height:158px">
    <div class="portrait" style="left:5px;top:5px;width:103px;height:68px" role="img" aria-label="Portrait of Ravi Menon"></div>
    <div class="name" style="top:78px;font-size:8px">Ravi Menon</div>
    <div class="role" style="top:91px;font-size:6px">Partner</div>
    <div class="bio" style="top:103px;font-size:6px">Strategy, partnerships and business development.</div>
    <div class="dot" style="left:51px;top:138px;width:11px;height:11px"></div>
  </div>

  <div class="contact-band" style="top:470px;height:180px;border-radius:16px 16px 0 0" role="img" aria-label="Faceted green shapes and a glass pyramid conservatory among trees">
    <svg class="abs" style="left:0;top:0" width="624" height="180" viewBox="0 0 624 180"><path d="M285 30 Q292 4 318 4 L475 4 Q500 4 494 28 L445 150 Q432 180 400 180 L262 180 Q240 180 248 158 Z" fill="#fff"/></svg>
  </div>
  <div class="contact-title" style="left:35px;top:487px;font-size:15px;width:150px">Let's Build Something Enduring Together</div>
  <div class="contact-text" style="left:35px;top:551px;width:160px;font-size:6.4px">We're always open to meaningful conversations. Reach out and let's explore how we can work together.</div>
  <div class="contact-line" style="left:35px;top:588px;font-size:6.4px"><i style="width:10px;height:10px"></i>+1 (415) 555-0143</div>
  <div class="contact-line" style="left:35px;top:606px;font-size:6.4px"><i style="width:10px;height:10px"></i>hello@verdanthold.com</div>
  <div class="contact-line" style="left:35px;top:624px;font-size:6.4px"><i style="width:10px;height:10px"></i>48 Lattice Way, Portland, OR 97205</div>
  <div class="form-title" style="left:285px;top:494px;font-size:12px"><svg width="13" height="13" viewBox="0 0 14 14"><path d="M7 1 L12.5 4 L12.5 10 L7 13 L1.5 10 L1.5 4 Z M1.5 4 L7 7 L12.5 4 M7 7 L7 13" fill="none" stroke="#1f3a1a" stroke-width="1.2"/></svg>Contact Info</div>
  <div class="field" style="left:277px;top:520px;width:92px;height:17px;font-size:5px">Full Name</div>
  <div class="field" style="left:375px;top:520px;width:96px;height:17px;font-size:5px">Email Address</div>
  <div class="field" style="left:277px;top:546px;width:194px;height:17px;font-size:5px">Company Name</div>
  <div class="field" style="left:277px;top:572px;width:194px;height:38px;font-size:5px">Your Message</div>
  <div class="btn" style="left:277px;top:619px;width:87px;height:17px;line-height:17px;font-size:6px">Send Message ➤</div>

  <div class="footer" style="height:109px">
    <div class="brand light" style="left:32px;top:12px;font-size:12px">Verdant</div>
    <div class="tag" style="left:32px;top:40px;width:110px;font-size:6.4px">Building lasting value through strategic investments and strong partnerships.</div>
    <h4 style="left:194px;top:14px;font-size:6.8px">Quick Links</h4>
    <div class="links" style="left:194px;top:28px;font-size:5.6px">Business Description<br>Investment Philosophy<br>Team<br>Contact Info</div>
    <h4 style="left:325px;top:14px;font-size:6.8px">Legal</h4>
    <div class="links" style="left:325px;top:28px;font-size:5.6px">Privacy Policy<br>Terms of Use<br>Disclaimer</div>
    <h4 style="left:439px;top:21px;font-size:6.8px">Follow Us</h4>
    <div class="social" style="left:439px;top:39px;gap:8px"><span style="width:18px;height:18px"></span><span style="width:18px;height:18px"></span><span style="width:18px;height:18px"></span><span style="width:18px;height:18px"></span></div>
    <div class="copy" style="top:88px;font-size:6.4px">© 2025 Company Name. All rights reserved.</div>
  </div>
</section>

<!-- TABLET -->
<section class="screen tablet" style="left:655px;width:334px">
  <div class="brand" style="left:24px;top:9px;font-size:12px">Verdant</div>
  <div class="burger" style="left:298px;top:14px"></div>
  <div class="hero" style="top:33px;height:151px" role="img" aria-label="Hero photograph of a green glass lattice roof structure">
    <svg class="abs" style="left:0;bottom:0" width="334" height="30" viewBox="0 0 334 30" preserveAspectRatio="none"><path d="M0 30 L0 22 C120 22 240 18 334 4 L334 30 Z" fill="#fff"/><path d="M160 22 C240 18 300 10 334 5" stroke="#5fa046" stroke-width="2" fill="none"/></svg>
  </div>
  <div class="hero-title" style="left:26px;top:65px;font-size:17px">Our <span>Team</span></div>
  <div class="hero-sub" style="left:26px;top:87px;font-size:7px">Built on experience. Focused on outcomes.</div>
  <div class="hero-text" style="left:26px;top:101px;width:150px;font-size:5.8px">A multidisciplinary team with deep expertise in investments, operations, and value creation. Together, we build enduring value.</div>
  <div class="btn" style="left:26px;top:144px;width:64px;height:15px;line-height:15px;font-size:5px">Contact Now</div>

  <div class="ornament" style="left:16px;top:200px;width:36px;height:36px" role="img" aria-label="Faint wireframe icosahedron ornament"></div>
  <div class="ornament" style="left:278px;top:196px;width:38px;height:38px" role="img" aria-label="Faint wireframe icosahedron ornament"></div>
  <div class="eyebrow" style="top:194px;font-size:5px">OUR STRENGTH</div>
  <div class="heading" style="top:203px;font-size:13px">The People Behind Our Purpose</div>
  <div class="lead" style="left:65px;width:204px;top:222px;font-size:5.6px">We combine decades of experience across investments, strategy, operations and finance to deliver consistent, long-term value.</div>

  <div class="card" style="left:14px;top:255px;width:90px;height:112px">
    <div class="portrait" style="left:3px;top:3px;width:84px;height:50px" role="img" aria-label="Portrait of Elliot Marsh"></div>
    <div class="name" style="top:56px;font-size:6px">Elliot Marsh</div><div class="role" style="top:65px;font-size:4.6px">Chief Executive Officer</div>
    <div class="bio" style="top:74px;font-size:4.6px">20+ years in investment leadership and value creation.</div>
    <div class="dot" style="left:40px;top:98px;width:9px;height:9px"></div>
  </div>
  <div class="card" style="left:112px;top:255px;width:90px;height:112px">
    <div class="portrait" style="left:3px;top:3px;width:84px;height:50px" role="img" aria-label="Portrait of Nora Whitfield"></div>
    <div class="name" style="top:56px;font-size:6px">Nora Whitfield</div><div class="role" style="top:65px;font-size:4.6px">Chief Investment Officer</div>
    <div class="bio" style="top:74px;font-size:4.6px">Expert in private markets and portfolio management.</div>
    <div class="dot" style="left:40px;top:98px;width:9px;height:9px"></div>
  </div>
  <div class="card" style="left:212px;top:255px;width:90px;height:112px">
    <div class="portrait" style="left:3px;top:3px;width:84px;height:50px" role="img" aria-label="Portrait of Owen Sinclair"></div>
    <div class="name" style="top:56px;font-size:6px">Owen Sinclair</div><div class="role" style="top:65px;font-size:4.6px">Head of Operations</div>
    <div class="bio" style="top:74px;font-size:4.6px">Operational excellence and driving scalable performance.</div>
    <div class="dot" style="left:40px;top:98px;width:9px;height:9px"></div>
  </div>
  <div class="card" style="left:61px;top:374px;width:90px;height:112px">
    <div class="portrait" style="left:3px;top:3px;width:84px;height:50px" role="img" aria-label="Portrait of Claire Holden"></div>
    <div class="name" style="top:56px;font-size:6px">Claire Holden</div><div class="role" style="top:65px;font-size:4.6px">Chief Financial Officer</div>
    <div class="bio" style="top:74px;font-size:4.6px">Financial strategy, risk management and governance.</div>
    <div class="dot" style="left:40px;top:98px;width:9px;height:9px"></div>
  </div>
  <div class="card" style="left:164px;top:374px;width:90px;height:112px">
    <div class="portrait" style="left:3px;top:3px;width:84px;height:50px" role="img" aria-label="Portrait of Ravi Menon"></div>
    <div class="name" style="top:56px;font-size:6px">Ravi Menon</div><div class="role" style="top:65px;font-size:4.6px">Partner</div>
    <div class="bio" style="top:74px;font-size:4.6px">Strategy, partnerships and business development.</div>
    <div class="dot" style="left:40px;top:98px;width:9px;height:9px"></div>
  </div>

  <div class="contact-band" style="top:496px;height:153px" role="img" aria-label="Faceted green shapes and a glass pyramid conservatory among trees">
    <svg class="abs" style="left:0;top:0" width="334" height="153" viewBox="0 0 334 153"><path d="M152 22 Q156 5 175 5 L268 5 Q286 5 282 24 L258 135 Q253 153 233 153 L150 153 Q136 153 139 136 Z" fill="#fff"/></svg>
  </div>
  <div class="contact-title" style="left:10px;top:508px;width:120px;font-size:10px">Let's Build Something Enduring Together</div>
  <div class="contact-text" style="left:10px;top:552px;width:118px;font-size:4.8px">We're always open to meaningful conversations. Reach out and let's explore how we can work together.</div>
  <div class="contact-line" style="left:10px;top:582px;font-size:4.8px"><i style="width:7px;height:7px"></i>+1 (415) 555-0143</div>
  <div class="contact-line" style="left:10px;top:595px;font-size:4.8px"><i style="width:7px;height:7px"></i>hello@verdanthold.com</div>
  <div class="contact-line" style="left:10px;top:608px;font-size:4.8px"><i style="width:7px;height:7px"></i>48 Lattice Way, Portland, OR 97205</div>
  <div class="form-title" style="left:160px;top:518px;font-size:8px"><svg width="9" height="9" viewBox="0 0 14 14"><path d="M7 1 L12.5 4 L12.5 10 L7 13 L1.5 10 L1.5 4 Z M1.5 4 L7 7 L12.5 4 M7 7 L7 13" fill="none" stroke="#1f3a1a" stroke-width="1.4"/></svg>Contact Info</div>
  <div class="field" style="left:160px;top:535px;width:54px;height:13px;font-size:4px">Full Name</div>
  <div class="field" style="left:218px;top:535px;width:54px;height:13px;font-size:4px">Email Address</div>
  <div class="field" style="left:160px;top:555px;width:112px;height:13px;font-size:4px">Company Name</div>
  <div class="field" style="left:160px;top:575px;width:112px;height:30px;font-size:4px">Your Message</div>
  <div class="btn" style="left:160px;top:613px;width:66px;height:12px;line-height:12px;font-size:4.6px">Send Message ➤</div>

  <div class="footer" style="height:110px">
    <div class="brand light" style="left:16px;top:12px;font-size:10px">Verdant</div>
    <div class="tag" style="left:16px;top:34px;width:85px;font-size:4.8px">Building lasting value through strategic investments and strong partnerships.</div>
    <h4 style="left:116px;top:12px;font-size:5px">Quick Links</h4>
    <div class="links" style="left:116px;top:22px;font-size:4.4px">Business Description<br>Investment Philosophy<br>Team<br>Contact Info</div>
    <h4 style="left:190px;top:12px;font-size:5px">Legal</h4>
    <div class="links" style="left:190px;top:22px;font-size:4.4px">Privacy Policy<br>Terms of Use<br>Disclaimer</div>
    <h4 style="left:252px;top:12px;font-size:5px">Follow Us</h4>
    <div class="social" style="left:248px;top:26px;gap:5px"><span style="width:12px;height:12px"></span><span style="width:12px;height:12px"></span><span style="width:12px;height:12px"></span><span style="width:12px;height:12px"></span></div>
    <div class="copy" style="top:88px;font-size:5px">© 2025 Company Name. All rights reserved.</div>
  </div>
</section>

<!-- MOBILE -->
<section class="screen mobile" style="left:1011px;width:176px">
  <div class="brand" style="left:16px;top:8px;font-size:10px">Verdant</div>
  <div class="burger" style="left:150px;top:10px;width:11px;height:9px"></div>
  <div class="hero" style="top:27px;height:138px" role="img" aria-label="Hero photograph of a green glass lattice roof structure">
    <svg class="abs" style="left:0;bottom:0" width="176" height="20" viewBox="0 0 176 20" preserveAspectRatio="none"><path d="M0 20 L0 14 C60 14 130 10 176 2 L176 20 Z" fill="#fff"/><path d="M90 14 C130 11 160 6 176 3" stroke="#5fa046" stroke-width="2" fill="none"/></svg>
  </div>
  <div class="hero-title" style="left:20px;top:49px;font-size:15px">Our <span>Team</span></div>
  <div class="hero-sub" style="left:20px;top:68px;width:120px;font-size:6px;line-height:1.5">Built on experience. Focused on outcomes.</div>
  <div class="hero-text" style="left:20px;top:93px;width:100px;font-size:4.8px">A multidisciplinary team with deep expertise in investments, operations, and value creation. Together, we build enduring value.</div>
  <div class="btn" style="left:20px;top:141px;width:54px;height:12px;line-height:12px;font-size:4.3px">Contact Now</div>

  <div class="ornament" style="left:14px;top:180px;width:28px;height:28px" role="img" aria-label="Faint wireframe icosahedron ornament"></div>
  <div class="ornament" style="left:136px;top:177px;width:29px;height:29px" role="img" aria-label="Faint wireframe icosahedron ornament"></div>
  <div class="eyebrow" style="top:180px;font-size:4px">OUR STRENGTH</div>
  <div class="heading" style="top:188px;font-size:8.5px;left:40px;right:40px">The People Behind Our Purpose</div>
  <div class="lead" style="left:36px;width:104px;top:215px;font-size:4.8px">We combine decades of experience across investments, strategy, operations and finance to deliver consistent, long-term value.</div>

  <div class="row" style="top:262px"><div class="portrait" role="img" aria-label="Portrait of Elliot Marsh"></div><div class="name">Elliot Marsh</div><div class="role">Chief Executive Officer</div><div class="dot"></div></div>
  <div class="row" style="top:296px"><div class="portrait" role="img" aria-label="Portrait of Nora Whitfield"></div><div class="name">Nora Whitfield</div><div class="role">Chief Investment Officer</div><div class="dot"></div></div>
  <div class="row" style="top:330px"><div class="portrait" role="img" aria-label="Portrait of Owen Sinclair"></div><div class="name">Owen Sinclair</div><div class="role">Head of Operations</div><div class="dot"></div></div>
  <div class="row" style="top:364px"><div class="portrait" role="img" aria-label="Portrait of Claire Holden"></div><div class="name">Claire Holden</div><div class="role">Chief Financial Officer</div><div class="dot"></div></div>
  <div class="row" style="top:398px"><div class="portrait" role="img" aria-label="Portrait of Ravi Menon"></div><div class="name">Ravi Menon</div><div class="role">Partner</div><div class="dot"></div></div>

  <div class="contact-band" style="top:440px;height:154px" role="img" aria-label="Dark green panel with a glass pyramid conservatory at the right"></div>
  <div class="contact-title" style="left:19px;top:453px;width:110px;font-size:8.5px">Let's Build Something Enduring Together</div>
  <div class="contact-text" style="left:19px;top:483px;width:95px;font-size:4.6px">We're always open to meaningful conversations.</div>
  <div class="contact-line" style="left:19px;top:507px;font-size:4.6px"><i style="width:6px;height:6px"></i>+1 (415) 555-0143</div>
  <div class="contact-line" style="left:19px;top:520px;font-size:4.6px"><i style="width:6px;height:6px"></i>hello@verdanthold.com</div>
  <div class="contact-line" style="left:19px;top:533px;font-size:4.6px;line-height:1.5"><i style="width:6px;height:6px"></i>48 Lattice Way,<br>Portland, OR 97205</div>
  <div class="btn outline" style="left:19px;top:562px;width:107px;height:24px;line-height:21px;font-size:8px">Contact Info</div>

  <div class="footer" style="height:165px">
    <div class="brand light" style="left:19px;top:14px;font-size:10px">Verdant</div>
    <div class="tag" style="left:19px;top:37px;width:110px;font-size:5.8px">Building lasting value through strategic investments and strong partnerships.</div>
    <div style="position:absolute;left:12px;right:12px;top:79px;border-top:1px solid #3a3a3a"></div>
    <h4 style="left:17px;top:88px;font-size:6px">Quick Links</h4>
    <h4 style="left:75px;top:88px;font-size:6px">Legal</h4>
    <h4 style="left:123px;top:88px;font-size:6px">Follow Us</h4>
    <div class="social" style="left:33px;top:103px;gap:8px"><span style="width:15px;height:15px"></span><span style="width:15px;height:15px"></span><span style="width:15px;height:15px"></span><span style="width:15px;height:15px"></span></div>
    <div style="position:absolute;left:12px;right:12px;top:131px;border-top:1px solid #3a3a3a"></div>
    <div class="copy" style="top:136px;font-size:5.4px;line-height:1.8">© 2025 Company Name.<br>All rights reserved.</div>
  </div>
</section>

</body>
</html>
```